Business Card Design

Need a hot business card in wine colors something cool and mod please feel free to be , FUNKY and free with this .

Industry/Entity Type

Business

Contact Information for Business Card

LUMERA HAIR DESIGN 3182 w 9th st scottsdale az 85619 Custom modern hair design and custom color by MARCUS OBRIDGE 602-4168203 cell salon 480 -712-6084 email marcusobridge@quillpost.com hours wed thru sat 7am to 6pm.

Font styles to use
Other font styles liked:
• something fun and mod.

Colors
a54599
6b449b
1b1b1b
606060

Requirements
Must have
• Apointment reminder on flip side of card.
Should not have
• Nothing boring.

```html
<!DOCTYPE html>
<html lang="en">
<head>
<meta charset="utf-8">
<title>Lumera Hair Design – Business Card</title>
<link rel="stylesheet" href="https://fonts.googleapis.com/css2?family=Cinzel:wght@400;600&family=Didact+Gothic&family=Dancing+Script:wght@500&display=swap">
<style>
  :root {
    --page: #ffffff;
    --card: #0d0d0d;
    --violet: #a54cf0;
    --violet-deep: #6b449b;
    --band-violet: #7a52e8;
    --grey: #606060;
    --text: #f4f4f4;
  }
  * { margin: 0; padding: 0; box-sizing: border-box; }
  html, body {
    width: 1200px; height: 417px; overflow: hidden;
    background: var(--page);
  }
  .canvas { position: relative; width: 1200px; height: 417px; }

  .card {
    position: absolute; top: 44px; height: 326px;
    background: var(--card); overflow: hidden;
    color: var(--text);
  }
  .card--front { left: 44px; width: 552px; }
  .card--back { left: 620px; width: 536px; }

  .ornament-area {
    position: absolute;
    background: linear-gradient(180deg, rgba(165,76,240,0.55), rgba(107,68,155,0.35));
    border-radius: 40px;
  }
  .card--front .ornament-area { left: 10px; top: 8px; width: 110px; height: 310px; }

  .brand-tag {
    position: absolute; left: 248px; top: 10px; width: 288px; height: 35px;
    background: var(--band-violet);
    font-family: "Cinzel", serif; font-size: 19px; letter-spacing: 0.5px;
    line-height: 35px; text-align: center; color: var(--text);
  }
  .rule {
    position: absolute; left: 106px; right: 0; height: 6px;
    background: var(--grey);
  }
  .rule--top { top: 51px; }
  .rule--bottom { top: 287px; }

  .tagline {
    position: absolute; left: 130px; width: 410px; top: 60px;
    font-family: "Dancing Script", cursive; font-size: 19px;
    line-height: 30px; text-align: center;
  }
  .stylist {
    position: absolute; left: 130px; width: 410px; top: 127px;
    font-family: "Didact Gothic", sans-serif; font-size: 21px;
    letter-spacing: 0.5px; text-align: center;
  }
  .contact {
    position: absolute; right: 18px; text-align: right;
    font-family: "Didact Gothic", sans-serif; color: var(--text);
  }
  .contact--phones { top: 164px; font-size: 20px; line-height: 27px; }
  .contact--address { top: 229px; font-size: 18px; line-height: 26px; }
  .hours {
    position: absolute; left: 170px; top: 298px;
    font-family: "Didact Gothic", sans-serif; font-size: 15.5px;
  }

  .card--back .ornament-area { left: 25px; width: 486px; }
  .ornament-area--top { top: 58px; height: 72px; }
  .ornament-area--bottom { top: 196px; height: 66px; }
  .name-band {
    position: absolute; left: 0; right: 0; top: 134px; height: 58px;
    background: var(--grey);
    font-family: "Cinzel", serif; font-size: 36px; letter-spacing: 2px;
    line-height: 58px; text-align: center; color: var(--text);
  }
</style>
</head>
<body>
<div class="canvas">
  <section class="card card--front">
    <div class="ornament-area" role="img" aria-label="Violet tribal flourish ornaments"></div>
    <div class="brand-tag">LUMERA HAIR DESIGN</div>
    <div class="rule rule--top"></div>
    <p class="tagline">Custom modern hair design and custom color<br>by:</p>
    <p class="stylist">MARCUS OBRIDGE</p>
    <p class="contact contact--phones">602-4168203<br>480 -712-6084</p>
    <p class="contact contact--address">3182 w 9th st scottsdale az 85619<br>marcusobridge@quillpost.com</p>
    <div class="rule rule--bottom"></div>
    <p class="hours">Opens: wed, thru, and sat 7am to 6pm</p>
  </section>

  <section class="card card--back">
    <div class="ornament-area ornament-area--top" role="img" aria-label="Mirrored violet tribal flourishes above the name"></div>
    <div class="name-band">Lumera Hair Design</div>
    <div class="ornament-area ornament-area--bottom" role="img" aria-label="Mirrored violet tribal flourishes below the name"></div>
  </section>
</div>
</body>
</html>
```